TORVEN RENEWABLES

New business B2B Energy Renewables website.
Please refer to our competitor https://www.quorbit72.co.uk/ for a similar website.

Need extra days to review

```html
<!DOCTYPE html>
<html lang="en">
<head>
<meta charset="utf-8">
<title>Torven Renewables</title>
<link href="https://fonts.googleapis.com/css2?family=Montserrat:wght@400;500;600;700;800;900&display=swap" rel="stylesheet">
<style>
:root{
  --blue:#1453b8;
  --blue-dark:#0b4aa8;
  --navy:#0d1b3e;
  --ink:#1a1a1a;
  --text:#333;
  --muted:#f3f6fa;
  --footer:#1e2024;
  --line:#d6dde8;
  --white:#fff;
}
*{margin:0;padding:0;box-sizing:border-box}
html,body{width:1200px;height:2920px;overflow:hidden}
body{font-family:"Montserrat",sans-serif;color:var(--text);background:var(--white);position:relative}
.abs{position:absolute}
/* header */
.site-header{position:absolute;left:0;top:0;width:1200px;height:87px;background:var(--white)}
.brand{left:88px;top:14px;display:flex;align-items:center;gap:10px}
.brand-mark{width:40px;height:40px;background:var(--navy)}
.brand-name{font-weight:800;font-size:18px;color:var(--navy);letter-spacing:1.5px;line-height:1.05}
.brand-name small{display:block;font-size:10px;letter-spacing:4px;font-weight:700}
.nav{left:455px;top:25px;display:flex;align-items:center;gap:0;font-size:15px;font-weight:500;color:var(--ink)}
.nav a{text-decoration:none;color:inherit;padding:9px 21px}
.nav .active{background:var(--blue-dark);color:var(--white);clip-path:polygon(0 0,92% 0,100% 100%,6% 100%);padding:9px 22px 9px 24px}
.call-box{left:945px;top:20px;width:167px;height:47px;border:1px solid var(--blue);display:flex;align-items:center;gap:10px;padding-left:16px}
.call-box .lbl{font-size:10px;color:var(--blue)}
.call-box .num{font-size:14px;font-weight:700;color:var(--navy)}
/* hero */
.hero{left:0;top:87px;width:1200px;height:447px;background:linear-gradient(180deg,#4d73a8 0%,#9db3cf 35%,#f2c98a 62%,#3d4a63 78%,#1c2740 100%)}
.hero-title{left:641px;top:150px;font-size:43px;font-weight:900;color:#11172a;line-height:1.13}
.btn-outline{border:2px solid var(--blue-dark);font-size:15px;font-weight:500;color:var(--ink);display:flex;align-items:center;justify-content:center;clip-path:polygon(0 0,100% 0,100% 100%,3% 100%)}
.hero .btn-outline{left:645px;top:275px;width:135px;height:37px}
.hero-arrow{top:210px}
/* about */
.section-title{font-size:34px;font-weight:800;color:var(--blue)}
.about-title{left:88px;top:640px}
.about-rule{left:88px;top:712px;width:3px;height:92px;background:var(--blue)}
.about-lead{left:137px;top:706px;width:490px;font-size:19.5px;font-weight:700;color:var(--ink);line-height:1.35}
.about-body{left:137px;top:780px;width:490px;font-size:13.4px;line-height:1.7;color:#222}
.about-body p+p{margin-top:19px}
.about .btn-outline{left:88px;top:967px;width:133px;height:37px}
.about-line{left:234px;top:986px;width:188px;height:1px;background:var(--line)}
.about-photo{left:672px;top:629px;width:440px;height:387px;background:linear-gradient(135deg,#4aa2e0,#8fc6ee 45%,#5f9b3f 75%,#1d3f8a)}
.about-photo-ext{left:516px;top:937px;width:160px;height:79px;background:linear-gradient(90deg,#4d8f5a,#2a55a8)}
/* services */
.services{left:0;top:1113px;width:1200px;height:502px;background:var(--muted)}
.services-dark{left:0;top:0;width:320px;height:502px;background:linear-gradient(180deg,#2e3a4e,#1a2233);clip-path:polygon(0 0,233px 0,320px 100%,0 100%)}
.services-title{left:288px;top:75px}
.slider-arrows{display:flex;gap:8px}
.services .slider-arrows{left:1052px;top:80px}
.service-card{top:155px;width:233px;height:242px}
.service-img{width:100%;height:100%;clip-path:polygon(0 0,86% 0,100% 100%,16% 100%)}
.service-label{top:262px;width:233px;text-align:center;font-size:16px;font-weight:600;color:var(--ink);letter-spacing:.3px}
/* solutions */
.solutions-title{left:88px;top:1735px;line-height:1.15}
.sol-card{top:1873px;width:216px;height:155px;border:1px solid var(--line);background:var(--white);display:flex;flex-direction:column;align-items:center;justify-content:center;gap:14px;text-align:center;font-size:15px;color:var(--blue);line-height:1.3}
.sol-photo{left:705px;top:1712px;width:407px;height:364px;background:linear-gradient(160deg,#dbe6f2,#9fb6d0 45%,#3a5d95 80%,#27324b)}
/* clients */
.clients{left:0;top:2173px;width:1200px;height:362px;background:var(--muted)}
.clients-title{left:0;top:65px;width:1200px;text-align:center}
.client-logo{top:138px;width:183px;height:82px;background:var(--white);display:flex;align-items:center;justify-content:center;gap:8px;font-size:20px;font-weight:700;color:#333}
.client-logo i{width:14px;height:14px;background:#333;display:block}
.clients .slider-arrows{left:568px;top:262px}
/* footer */
.footer{left:0;top:2535px;width:1200px;height:345px;background:linear-gradient(180deg,#2a2c31,var(--footer))}
.footer h4{position:absolute;top:60px;font-size:19px;font-weight:600;color:var(--blue)}
.f-small{font-size:13px;color:var(--white);line-height:1.5}
.f-label{font-size:12.5px;color:var(--blue)}
.f-links a{display:block;color:var(--white);text-decoration:none;font-size:13.5px;line-height:27px}
.f-links a.on{color:var(--blue);text-decoration:underline}
.field{background:var(--white);height:38px;width:275px;display:flex;align-items:center;gap:8px;padding-left:10px;font-size:12px;color:#888}
.submit{left:543px;top:261px;width:108px;height:34px;background:var(--blue);color:var(--white);font-weight:600;font-size:14px;display:flex;align-items:center;justify-content:center;clip-path:polygon(3% 0,100% 0,97% 100%,0 100%)}
.bottom-bar{left:0;top:2880px;width:1200px;height:40px;background:var(--blue);color:var(--white);font-size:13.5px;display:flex;align-items:center;justify-content:space-between;padding:0 88px}
.socials{display:flex;gap:16px}
.socials i{width:10px;height:10px;border-radius:50%;background:var(--white);display:block}
</style>
</head>
<body>

<header class="site-header">
  <div class="abs brand">
    <div class="brand-mark"></div>
    <div class="brand-name">TORVEN<small>RENEWABLES</small></div>
  </div>
  <nav class="abs nav">
    <a class="active" href="#">Home</a>
    <a href="#">About Us</a>
    <a href="#">Services</a>
    <a href="#">Contact Us</a>
  </nav>
  <div class="abs call-box">
    <svg width="22" height="22" viewBox="0 0 24 24" fill="none" stroke="#1453b8" stroke-width="1.6"><path d="M5 3h4l2 5-2.5 1.5a11 11 0 0 0 6 6L16 13l5 2v4a2 2 0 0 1-2 2A17 17 0 0 1 3 5a2 2 0 0 1 2-2z"/></svg>
    <div><div class="lbl">Call Us:</div><div class="num">555-204-7318</div></div>
  </div>
</header>

<section class="abs hero" role="img" aria-label="Wind turbines and solar panel rows at sunset">
  <svg class="abs hero-arrow" style="left:70px" width="20" height="36" viewBox="0 0 20 36"><path d="M18 2 2 18l16 16" fill="none" stroke="#0d1b3e" stroke-width="2"/></svg>
  <h1 class="abs hero-title">Improving Solar<br>Energy Products</h1>
  <div class="abs btn-outline">Get a Quote</div>
  <svg class="abs hero-arrow" style="left:1110px" width="20" height="36" viewBox="0 0 20 36"><path d="M2 2l16 16L2 34" fill="none" stroke="#1453b8" stroke-width="2"/></svg>
</section>

<section class="about">
  <h2 class="abs section-title about-title">About Us</h2>
  <div class="abs about-rule"></div>
  <p class="abs about-lead">Lorem Ipsum is simply dummy text of the print-ing and typesetting industry.</p>
  <div class="abs about-body">
    <p>Lorem Ipsum has been the industry's standard dummy text ever since the 1500s, when an unknown printer took a galley of type and scrambled it to make a type specimen book.</p>
    <p>It has survived not only five centuries, but also the leap into electronic type-setting, remaining essentially unchanged.</p>
  </div>
  <div class="abs btn-outline">Read More</div>
  <div class="abs about-line"></div>
  <div class="abs about-photo-ext" role="img" aria-label="Hands typing on a laptop over solar panels"></div>
  <div class="abs about-photo" role="img" aria-label="Engineer at a laptop with wind turbines on green hills"></div>
</section>

<section class="abs services">
  <div class="abs services-dark" role="img" aria-label="Workers installing solar panels"></div>
  <h2 class="abs section-title services-title">Our Services</h2>
  <div class="abs slider-arrows">
    <svg width="26" height="26" viewBox="0 0 26 26"><circle cx="13" cy="13" r="12" fill="none" stroke="#9fb6d8"/><path d="M18 13H8m4-4-4 4 4 4" fill="none" stroke="#9fb6d8" stroke-width="1.4"/></svg>
    <svg width="26" height="26" viewBox="0 0 26 26"><circle cx="13" cy="13" r="12" fill="none" stroke="#111" stroke-width="1.4"/><path d="M8 13h10m-4-4 4 4-4 4" fill="none" stroke="#111" stroke-width="1.4"/></svg>
  </div>
  <div class="abs service-card" style="left:234px"><div class="service-img" style="background:linear-gradient(135deg,#6f9a55,#2c3d63)" role="img" aria-label="Consultants shaking hands over a solar panel"></div></div>
  <div class="abs service-card" style="left:455px"><div class="service-img" style="background:linear-gradient(135deg,#e7ebef,#27407f)" role="img" aria-label="Solar panel model on design plans"></div></div>
  <div class="abs service-card" style="left:675px"><div class="service-img" style="background:linear-gradient(135deg,#d9dde2,#7c8088)" role="img" aria-label="Model house with solar roof and calculator"></div></div>
  <div class="abs service-card" style="left:895px"><div class="service-img" style="background:linear-gradient(135deg,#8fb3dd,#2b4f95 60%,#e3c224)" role="img" aria-label="Technician installing solar panels"></div></div>
  <div class="abs service-label" style="left:254px">Consulting</div>
  <div class="abs service-label" style="left:475px">Design</div>
  <div class="abs service-label" style="left:695px">Finance</div>
  <div class="abs service-label" style="left:915px">Installation</div>
</section>

<section class="solutions">
  <h2 class="abs section-title solutions-title">Renewable Solutions to<br>include sections on</h2>
  <div class="abs sol-photo" role="img" aria-label="Engineer in hard hat working on a solar panel"></div>
  <div class="abs sol-card" style="left:88px">
    <svg width="54" height="54" viewBox="0 0 54 54" fill="none" stroke="#222" stroke-width="1.6"><circle cx="40" cy="12" r="5"/><path d="M40 2v3M40 19v3M30 12h3M47 12h3"/><path d="M16 8v44M16 8l-8 10M16 8l8 8"/><path d="M22 28h24l3 18H19z"/><path d="M20 37h28M30 28l-2 18M38 28l1 18"/></svg>
    <span>Various Renewables<br>Offered</span>
  </div>
  <div class="abs sol-card" style="left:328px">
    <svg width="54" height="54" viewBox="0 0 54 54" fill="none" stroke="#222" stroke-width="1.6"><path d="M30 10 20 28h10l-6 16 12-20H26z"/><path d="M27 2v4M27 48v4M6 27h4M44 27h4M12 12l3 3M39 39l3 3M42 12l-3 3M12 42l3-3"/></svg>
    <span>Energy Saving<br>Assessment</span>
  </div>
  <div class="abs sol-card" style="left:568px">
    <svg width="54" height="54" viewBox="0 0 54 54" fill="none" stroke="#222" stroke-width="1.6"><rect x="4" y="8" width="46" height="32" rx="2"/><path d="M10 30l8-9 8 5 8-10 8 6"/><path d="M20 40v6h14v-6M16 46h22"/></svg>
    <span>Monitoring</span>
  </div>
</section>

<section class="abs clients">
  <h2 class="abs section-title clients-title">Our Clients</h2>
  <div class="abs client-logo" style="left:88px"><i></i>Norvell</div>
  <div class="abs client-logo" style="left:298px">Brightway Standards</div>
  <div class="abs client-logo" style="left:508px">Ledgerline Guild</div>
  <div class="abs client-logo" style="left:718px">Kestra</div>
  <div class="abs client-logo" style="left:928px">Oravo</div>
  <div class="abs slider-arrows">
    <svg width="26" height="26" viewBox="0 0 26 26"><circle cx="13" cy="13" r="12" fill="none" stroke="#9fb6d8"/><path d="M18 13H8m4-4-4 4 4 4" fill="none" stroke="#9fb6d8" stroke-width="1.4"/></svg>
    <svg width="26" height="26" viewBox="0 0 26 26"><circle cx="13" cy="13" r="12" fill="none" stroke="#111" stroke-width="1.4"/><path d="M8 13h10m-4-4 4 4-4 4" fill="none" stroke="#111" stroke-width="1.4"/></svg>
  </div>
</section>

<footer class="abs footer">
  <h4 style="left:88px">Conatct Info</h4>
  <div class="abs f-label" style="left:88px;top:102px">CALL US:</div>
  <div class="abs f-small" style="left:88px;top:126px;display:flex;gap:12px;align-items:center">
    <svg width="12" height="12" viewBox="0 0 24 24" fill="#1453b8"><path d="M5 2h4l2 6-3 2a12 12 0 0 0 6 6l2-3 6 2v4a3 3 0 0 1-3 3A19 19 0 0 1 2 5a3 3 0 0 1 3-3z"/></svg>(555) 410-2286</div>
  <div class="abs f-small" style="left:88px;top:151px;display:flex;gap:12px;align-items:center">
    <svg width="12" height="10" viewBox="0 0 12 10"><rect width="12" height="10" fill="#1453b8"/><path d="M0 0l6 5 6-5" fill="none" stroke="#fff"/></svg>hello@torvenrenewable.com</div>
  <div class="abs f-label" style="left:90px;top:194px">ADDRESS:</div>
  <div class="abs f-small" style="left:90px;top:218px;font-size:12.5px">42 Lorem Ipsum<br>Alderton, Westvale 40217</div>

  <h4 style="left:346px">Quick Link</h4>
  <div class="abs f-links" style="left:346px;top:99px">
    <a class="on" href="#">Home</a><a href="#">About Us</a><a href="#">Services</a><a href="#">Contact Us</a>
  </div>

  <h4 style="left:541px">Quick inquiry</h4>
  <div class="abs field" style="left:543px;top:106px"><svg width="12" height="12" viewBox="0 0 12 12" fill="none" stroke="#1453b8"><circle cx="6" cy="4" r="3"/><path d="M1 12a5 5 0 0 1 10 0"/></svg>Name</div>
  <div class="abs field" style="left:543px;top:156px"><svg width="12" height="10" viewBox="0 0 12 10" fill="none" stroke="#1453b8"><rect x=".5" y=".5" width="11" height="9"/><path d="M.5.5l5.5 5 5.5-5"/></svg>Email</div>
  <div class="abs field" style="left:543px;top:207px"><svg width="10" height="13" viewBox="0 0 10 13" fill="none" stroke="#1453b8"><rect x=".5" y=".5" width="9" height="12" rx="1"/></svg>Phone</div>
  <div class="abs field" style="left:834px;top:106px;height:139px;align-items:flex-start;padding-top:12px"><svg width="12" height="12" viewBox="0 0 12 12" fill="none" stroke="#1453b8"><path d="M.5.5h11v8h-7l-3 3v-3h-1z"/></svg>Message</div>
  <div class="abs submit">Submit</div>
</footer>

<div class="abs bottom-bar">
  <span>Copyright © 2022 Torven Renewable. All Rights Reserved</span>
  <div class="socials" aria-label="Social links"><i></i><i></i><i></i><i></i></div>
</div>

</body>
</html>
```